" Somos uma pequena empresa familiar localizada na Barra da Tijuca, Rio de Janeiro. Realizamos a intermediaçao na compra e venda de imóveis, locaçoes, somos correspondentes bancários do venturim, urupê e fundo solar. Entendo que a chave do sucesso no ramo imobiliário é a confiança deposita pelos nossos clientes. Preciso que a imagem da minha empresa inspire a confiança. "

```html
<!DOCTYPE html>
<html lang="pt-BR">
<head>
<meta charset="utf-8">
<title>Lume Imóveis — Cartão de visita</title>
<link href="https://fonts.googleapis.com/css2?family=Open+Sans:wght@400;600&display=swap" rel="stylesheet">
<style>
  :root {
    --backdrop: #2b2b2d;
    --navy: #1f3f73;
    --navy-deep: #173260;
    --navy-light: #2b5290;
    --paper: #ffffff;
    --paper-shade: #dcdde0;
    --ink: #5d6066;
    --ink-soft: #9a9ca1;
    --on-navy: #e6ecf6;
    --on-navy-soft: #a9bad6;
  }
  * { box-sizing: border-box; margin: 0; padding: 0; }
  html, body { width: 1200px; height: 1200px; overflow: hidden; }
  body {
    background: var(--backdrop);
    font-family: "Open Sans", Arial, sans-serif;
    display: flex;
    flex-direction: column;
    align-items: center;
    justify-content: center;
    gap: 60px;
  }
  .card {
    width: 900px;
    height: 500px;
    border-radius: 6px;
    overflow: hidden;
    position: relative;
    box-shadow: 0 14px 30px rgba(0,0,0,.45);
  }

  /* Front */
  .card-front { display: flex; flex-direction: column; }
  .front-face {
    flex: 1;
    background: linear-gradient(160deg, var(--paper) 40%, var(--paper-shade));
    display: flex;
    align-items: center;
    justify-content: center;
  }
  .brand { display: flex; align-items: center; gap: 22px; }
  .brand-mark { width: 70px; height: 70px; background: var(--navy); }
  .brand-text { display: flex; flex-direction: column; }
  .brand-name {
    font-size: 84px;
    font-weight: 600;
    color: var(--navy);
    letter-spacing: 6px;
    line-height: 1;
  }
  .brand-license {
    margin-top: 12px;
    font-size: 19px;
    color: var(--ink);
    letter-spacing: 3px;
  }
  .front-band {
    height: 130px;
    background: linear-gradient(90deg, var(--navy-deep), var(--navy-light));
    color: var(--on-navy);
    padding: 26px 44px;
    display: flex;
    flex-direction: column;
    justify-content: center;
    gap: 10px;
    font-size: 19px;
  }
  .front-band .row { display: flex; justify-content: space-between; }
  .front-band strong { font-weight: 600; }

  /* Back */
  .card-back {
    background: linear-gradient(150deg, var(--navy-light), var(--navy-deep));
    color: var(--on-navy);
    padding: 48px 56px;
    display: flex;
    flex-direction: column;
    align-items: flex-end;
    text-align: right;
  }
  .holder-name { font-size: 40px; font-weight: 400; }
  .holder-role { font-size: 15px; color: var(--on-navy-soft); margin-top: 4px; }
  .contact-list { list-style: none; margin-top: 34px; display: flex; flex-direction: column; gap: 10px; font-size: 20px; }
  .contact-list li { display: flex; align-items: center; justify-content: flex-end; gap: 14px; }
  .contact-list .spacer { height: 16px; }
  .contact-icon { width: 18px; height: 18px; flex: none; }
  .contact-dot { width: 14px; height: 14px; border-radius: 50%; background: var(--on-navy-soft); flex: none; margin: 0 2px; }
  .website { margin-top: auto; font-size: 22px; font-weight: 600; }
</style>
</head>
<body>
  <section class="card card-front" aria-label="Frente do cartão">
    <div class="front-face">
      <div class="brand">
        <div class="brand-mark"></div>
        <div class="brand-text">
          <span class="brand-name">LUME IMÓVEIS</span>
          <span class="brand-license">CRECI JURÍDICO 4521</span>
        </div>
      </div>
    </div>
    <div class="front-band">
      <div class="row"><span>Av. das Palmeiras, 210 · CEP 00000-000 · Barra RJ</span></div>
      <div class="row">
        <span>T.: <strong>(00) 0000.0000</strong></span>
        <span>contato@<strong>lumeimoveis</strong>.com.br</span>
        <span>www.<strong>lumeimoveis</strong>.com.br</span>
      </div>
    </div>
  </section>

  <section class="card card-back" aria-label="Verso do cartão">
    <h1 class="holder-name">Nome e Sobrenome</h1>
    <p class="holder-role">Cargo / Função</p>
    <ul class="contact-list">
      <li>contato@seudominio.com.br
        <svg class="contact-icon" viewBox="0 0 18 18"><rect x="1" y="4" width="16" height="11" fill="none" stroke="#a9bad6" stroke-width="1.6"/><path d="M1 4l8 6 8-6" fill="none" stroke="#a9bad6" stroke-width="1.6"/></svg>
      </li>
      <li>rede.com/seunome <span class="contact-dot"></span></li>
      <li>@seuperfil <span class="contact-dot"></span></li>
      <li class="spacer"></li>
      <li>T.: (00) 0000.0000
        <svg class="contact-icon" viewBox="0 0 18 18"><path d="M4 2l3 3-2 2c1 2 3 4 5 5l2-2 3 3-2 3C8 16 2 10 1 4z" fill="#a9bad6"/></svg>
      </li>
      <li>T.: (00) 0000.0000
        <svg class="contact-icon" viewBox="0 0 18 18"><path d="M4 2l3 3-2 2c1 2 3 4 5 5l2-2 3 3-2 3C8 16 2 10 1 4z" fill="#a9bad6"/></svg>
      </li>
    </ul>
    <p class="website">www.lumeimoveis.com.br</p>
  </section>
</body>
</html>
```